Modern, Sleek & Vibrant design required for electrical contracting work.

I require a flyer design for VORNAL ELECTRO SERVICES, which operates as an electrical contractor. We do electrical installations such as LED lighting, maintenance, repairs, communications and various other work related for residential and commercial customers. I would like the same colours applied from my logo to the flyer (Electric Blue, White, Grey/Silver). A6 or DL sizes with single side.

Target Market(s)

Residential and Commercial customers.

Industry/Entity Type

Communications

Font styles to use
Serif
Sans Serif

Requirements
Must have
• My logo and colours (Electric Blue, White, Silver/Grey)
Nice to have
• Shapes separating different parts of the flyer, such as the same electric bolt from my logo. Straight or angled shapes.
Should not have
• Childish pictures such as light bulbs. Curved shapes.

```html
<!DOCTYPE html>
<html lang="en">
<head>
<meta charset="utf-8">
<title>Vornal Electro Services – Flyer</title>
<link rel="stylesheet" href="https://fonts.googleapis.com/css2?family=Oswald:wght@400;500;600;700&display=swap">
<style>
  :root {
    --page-bg: #e6e5e2;
    --navy-deep: #050b1c;
    --navy: #0b1f44;
    --electric-blue: #1d6fc4;
    --electric-bright: #3aa2f0;
    --band-blue: #2b3fae;
    --silver-light: #f4f5f6;
    --silver: #c9cdd2;
    --silver-dark: #9aa0a7;
    --white: #ffffff;
  }
  * { margin: 0; padding: 0; box-sizing: border-box; }
  html, body {
    width: 1200px;
    height: 1148px;
    overflow: hidden;
    background: var(--page-bg);
    font-family: "Oswald", "Arial Narrow", sans-serif;
  }
  .flyer {
    position: absolute;
    left: 200px;
    top: 20px;
    width: 800px;
    height: 1108px;
    overflow: hidden;
    color: var(--white);
    background:
      radial-gradient(ellipse 70% 45% at 20% 8%, rgba(58,162,240,0.85), rgba(58,162,240,0) 70%),
      radial-gradient(ellipse 60% 40% at 55% 55%, rgba(29,111,196,0.55), rgba(29,111,196,0) 75%),
      linear-gradient(180deg, var(--electric-blue) 0%, var(--navy) 45%, var(--navy-deep) 100%);
  }
  .brand {
    position: absolute;
    left: 60px;
    top: 70px;
    display: flex;
    align-items: center;
    gap: 20px;
  }
  .brand-mark {
    width: 92px;
    height: 92px;
    border-radius: 50%;
    background: var(--silver);
    flex: none;
  }
  .brand-name {
    color: var(--white);
    font-size: 46px;
    font-weight: 600;
    line-height: 1;
    text-transform: uppercase;
    white-space: nowrap;
  }
  .tagline {
    position: absolute;
    right: 70px;
    top: 196px;
    font-size: 24px;
    font-weight: 500;
    letter-spacing: 0.5px;
  }
  .intro {
    position: absolute;
    left: 0;
    right: 0;
    top: 256px;
    text-align: center;
    font-size: 36px;
    font-weight: 500;
  }
  .service-band {
    position: absolute;
    left: 0;
    right: 0;
    top: 316px;
    height: 112px;
    background: linear-gradient(180deg, var(--silver-light) 0%, var(--white) 40%, var(--silver) 100%);
    display: flex;
    align-items: center;
    justify-content: center;
    text-align: center;
  }
  .service-band h1 {
    color: var(--band-blue);
    font-size: 44px;
    font-weight: 600;
    line-height: 1.05;
    text-transform: uppercase;
  }
  .service-list {
    position: absolute;
    left: 0;
    right: 0;
    top: 450px;
    list-style: none;
    text-align: center;
  }
  .service-list li {
    font-size: 68px;
    font-weight: 600;
    line-height: 82px;
    text-transform: uppercase;
    text-shadow: 0 3px 6px rgba(0,0,0,0.55);
  }
  .contact {
    position: absolute;
    left: 0;
    right: 0;
    top: 968px;
    text-align: center;
    font-size: 20px;
    font-weight: 400;
    font-style: normal;
    line-height: 25px;
    text-transform: uppercase;
  }
</style>
</head>
<body>
  <main class="flyer">
    <header class="brand">
      <span class="brand-mark" aria-hidden="true"></span>
      <p class="brand-name">Vornal Electro Services</p>
    </header>
    <p class="tagline">ELECTRICAL CONTRACTOR</p>

    <p class="intro">WHAT WE PROVIDE ?</p>
    <section class="service-band">
      <h1>We do electrical<br>installations</h1>
    </section>

    <ul class="service-list">
      <li>LED Lighting</li>
      <li>Installations</li>
      <li>Maintenance</li>
      <li>Repairs</li>
      <li>Communications</li>
      <li>Emergency Call-Outs</li>
    </ul>

    <address class="contact">
      EC Number – EC20934<br>
      Darren Velko (Director)<br>
      darren@vornalelectro.com<br>
      Company Name – Vornal Electro Services
    </address>
  </main>
</body>
</html>
```